Website To Serve As A Resource For Medical Conditions

I need a website that is attractive that will be utilized to educate patients on either hepatitis c or HIV so it should be easily readable attractive but also professional. This website is going to be furnished with various topics for example, HIV treatment, HIV and Nutrition, HIV and Exercise, HIV and....

This website will also be cloned and utilized similarly for Hepatitis.

Coded - Design and coding required

1 page

0094D4
00A9DD
6FCCEA
C7EBF8
E9F6FB
A7469A
B969AE
D3A5CF
EDDBEB
F8F0F9
6B429C
8869AF
B7A5CE
E3DAEB
F3F0F8

```html
<!DOCTYPE html>
<html lang="en">
<head>
<meta charset="utf-8">
<title>HIV Learning Hub</title>
<link href="https://fonts.googleapis.com/css2?family=Barlow+Condensed:wght@300;400;600&family=Poppins:wght@400;500;600&display=swap" rel="stylesheet">
<style>
:root{
  --blue-deep:#0094D4;--blue:#00A9DD;--blue-soft:#6FCCEA;--blue-pale:#C7EBF8;--blue-mist:#E9F6FB;
  --magenta:#A7469A;--magenta-soft:#B969AE;--magenta-pale:#D3A5CF;--magenta-mist:#EDDBEB;
  --purple:#6B429C;--purple-soft:#8869AF;--purple-pale:#B7A5CE;--lavender:#E3DAEB;--lavender-mist:#F3F0F8;
  --ink:#1b1b1f;--text:#444;--muted:#666;
}
*{box-sizing:border-box;margin:0;padding:0}
html,body{width:1200px;height:4577px;overflow:hidden}
body{font-family:'Poppins',sans-serif;color:var(--text);background:#fff;font-size:13px}
.wrap{width:876px;margin:0 auto;position:relative;height:100%}
section,header,footer{position:relative;overflow:hidden}
.heading{font-family:'Barlow Condensed',sans-serif;font-weight:300;color:var(--blue-deep);line-height:1}
.heading b{font-weight:600;color:var(--ink)}
.btn{display:inline-flex;align-items:center;justify-content:center;gap:6px;border-radius:24px;color:#fff;font-size:13px;font-weight:500;text-transform:uppercase;letter-spacing:.2px;text-decoration:none;white-space:nowrap}
.btn-blue{background:var(--blue-deep)}
.btn-purple{background:var(--magenta)}
.more{color:var(--magenta);font-size:11px;font-weight:500;text-decoration:none;text-transform:uppercase}

/* header */
.site-header{height:76px;border-top:3px solid var(--purple);background:#fff;box-shadow:0 1px 0 #eee}
.brand{position:absolute;left:0;top:18px;display:flex;align-items:center;gap:12px;font-family:'Barlow Condensed',sans-serif;font-weight:600;font-size:34px;color:var(--ink);text-decoration:none;white-space:nowrap}
.brand-dot{width:30px;height:30px;border-radius:50%;background:var(--magenta-soft)}
.nav{position:absolute;right:0;top:26px;display:flex;gap:36px;list-style:none;font-size:13.5px}
.nav a{color:var(--ink);text-decoration:none}
.nav a.active{color:var(--blue-deep);font-weight:500}

/* hero */
.hero{height:502px;background:linear-gradient(100deg,#141417 0%,#2a2a30 45%,#1e1e22 100%)}
.hero-photo{position:absolute;right:0;top:0;width:560px;height:100%;background:radial-gradient(ellipse at 55% 45%,#8a1414 0%,#3a1a1c 35%,#1e1e22 70%)}
.hero-body{position:absolute;left:0;top:196px;width:480px;display:flex;flex-direction:column;align-items:flex-start}
.hero-title{font-size:70px;color:var(--blue);white-space:nowrap}
.hero-title b{color:#fff}
.hero-text{margin-top:16px;color:#fff;font-size:14px;line-height:1.75}
.hero .btn{margin-top:28px;width:158px;height:42px}

/* what is */
.what{height:578px}
.what-frame{position:absolute;left:0;top:76px;width:395px;height:413px;border:6px solid var(--magenta-soft)}
.what-photo{position:absolute;left:14px;top:90px;width:398px;height:413px;background:radial-gradient(circle at 50% 45%,#e3564a 0%,#9fc7e6 25%,#3d8fd0 55%,#0c4a8c 100%)}
.what-body{position:absolute;left:473px;top:105px;width:403px}
.what-body h2{font-size:38px;margin-bottom:20px}
.what-body .lead{color:var(--ink);font-weight:600;font-size:14px;line-height:1.6;margin-bottom:12px}
.what-body .lead span{color:var(--blue-deep)}
.what-body p{font-size:13px;line-height:1.65;margin-bottom:10px}
.what-body p strong{color:var(--ink)}
.what-body .btn{margin-top:14px;width:158px;height:42px}

/* topics */
.topics{height:1111px;background:var(--lavender-mist)}
.section-title{text-align:center;font-size:40px;padding-top:74px}
.section-sub{text-align:center;font-size:16px;color:var(--text);margin-top:18px}
.cards{position:absolute;left:0;top:186px;display:grid;grid-template-columns:repeat(3,277px);gap:21px 22px}
.card{background:#fff;height:377px;text-align:center;box-shadow:0 2px 6px rgba(0,0,0,.05)}
.card-img{height:187px}
.card h3{font-size:16px;font-weight:600;color:var(--ink);margin-top:24px}
.card h3::after{content:"";display:block;width:34px;height:2px;background:var(--blue-soft);margin:12px auto 16px}
.card p{font-size:12.5px;line-height:1.6;padding:0 16px;height:62px}
.card .more{display:inline-block;margin-top:8px}
.topics .btn{position:absolute;left:361px;top:992px;width:154px;height:44px}

/* call to action */
.cta{height:355px;background:linear-gradient(90deg,var(--purple) 0%,#7b4aa6 60%,var(--purple) 100%)}
.cta-hands{position:absolute;left:0;top:0;width:355px;height:355px;background:radial-gradient(ellipse at 45% 50%,#d43c34 0%,#c99888 30%,rgba(107,66,156,0) 70%)}
.cta-people{position:absolute;right:0;top:70px;width:355px;height:215px;background:radial-gradient(ellipse at 50% 55%,#ffffff 0%,#e6dcf0 35%,rgba(107,66,156,0) 72%)}
.cta-body{position:absolute;left:0;right:0;top:70px;text-align:center}
.cta-body h2{font-size:52px;color:#fff}
.cta-body h2 b{color:#fff}
.cta-body p{color:#fff;font-size:18px;line-height:1.75;margin-top:18px}
.cta-body .btn{margin-top:22px;width:286px;height:52px;font-size:16px;background:var(--blue)}

/* stages */
.stages{height:711px}
.stages .section-title{padding-top:70px}
.video{position:absolute;left:32px;top:185px;width:810px;height:452px;background:#fff;padding:9px;box-shadow:0 2px 12px rgba(0,0,0,.14)}
.video-still{width:100%;height:100%;background:linear-gradient(120deg,#1d3348 0%,#4e6780 40%,#a57b63 60%,#2b3f52 100%)}
.play{position:absolute;left:50%;top:50%;transform:translate(-50%,-50%)}

/* blogs */
.blogs{height:753px;background:var(--lavender-mist)}
.blogs .section-title{padding-top:68px}
.feature{position:absolute;left:0;top:143px;width:426px}
.feature-img{height:263px;background:linear-gradient(135deg,#e9eef2 0%,#c9d3da 50%,#f3f1ee 100%)}
.meta{font-size:10.5px;color:#999;margin-top:28px}
.meta span{color:var(--blue-deep);padding-right:10px;margin-right:10px;border-right:1px solid #ccc}
.feature h3{font-size:15px;font-weight:600;color:var(--ink);line-height:1.4;margin-top:12px}
.feature p{font-size:12.5px;line-height:1.65;margin-top:12px}
.feature .more{display:inline-block;margin-top:16px}
.posts{position:absolute;left:470px;top:143px;width:406px}
.post{display:flex;gap:24px;height:163px}
.post-img{width:148px;height:128px;flex:none}
.post .meta{margin-top:0}
.post h4{font-size:13.5px;font-weight:600;color:var(--ink);line-height:1.35;margin-top:10px}
.post p{font-size:11.5px;line-height:1.6;margin-top:8px}
.post .more{display:inline-block;margin-top:8px}
.blogs .btn{position:absolute;left:361px;top:635px;width:154px;height:44px}

/* newsletter */
.newsletter{height:151px;background:var(--purple)}
.newsletter h2{position:absolute;left:0;top:42px;font-size:32px;color:#fff;white-space:nowrap}
.newsletter h2 b{color:#fff}
.newsletter p{position:absolute;left:0;top:90px;color:#fff;font-size:14px}
.signup{position:absolute;right:0;top:49px;width:370px;height:52px;background:#fff;border-radius:28px;display:flex;align-items:center}
.signup span{flex:1;padding-left:24px;color:#777;font-size:13px;display:flex;align-items:center;gap:10px}
.signup .btn{width:140px;height:52px;font-size:16px;background:var(--blue)}

/* footer */
.site-footer{height:340px;background:#fff}
.site-footer .brand{top:56px;font-size:32px}
.foot-about{position:absolute;left:0;top:128px;width:240px;font-size:12px;line-height:1.75}
.foot-about strong{color:var(--ink)}
.foot-about .more{display:inline-block;margin-top:12px}
.foot-col{position:absolute;top:80px}
.foot-col h5{font-family:'Barlow Condensed',sans-serif;font-weight:400;font-size:22px;color:var(--ink);margin-bottom:16px}
.foot-col h5 b{font-weight:600}
.foot-col ul{list-style:none;font-size:12px;line-height:26px}
.foot-col ul a{color:var(--text);text-decoration:none}
.foot-col ul a.active{color:var(--blue-deep);font-weight:500}
.contact-row{display:flex;gap:12px;font-size:12px;line-height:1.6;margin-bottom:14px}
.contact-row strong{color:var(--ink);font-size:14px;font-weight:500}
.social{display:flex;align-items:center;gap:12px;font-size:11px;text-transform:uppercase;margin-bottom:12px}
.social i{width:34px;height:34px;border-radius:50%;background:var(--purple-pale)}
.social:first-of-type i{background:var(--purple)}
.copyright{position:absolute;left:0;right:0;bottom:0;height:44px;border-top:1px solid #eee;text-align:center;font-size:12px;line-height:44px}
</style>
</head>
<body>

<header class="site-header">
  <div class="wrap">
    <a class="brand" href="#"><span class="brand-dot"></span>HIV Learning Hub</a>
    <ul class="nav">
      <li><a class="active" href="#">Home</a></li>
      <li><a href="#">HIV</a></li>
      <li><a href="#">Treatment</a></li>
      <li><a href="#">Prevention</a></li>
      <li><a href="#">Resources</a></li>
      <li><a href="#">Contact</a></li>
    </ul>
  </div>
</header>

<section class="hero">
  <div class="hero-photo" role="img" aria-label="Hand pinning a red awareness ribbon to a dark shirt"></div>
  <div class="wrap">
    <div class="hero-body">
      <h1 class="heading hero-title">HIV <b>Learning Hub</b></h1>
      <p class="hero-text">The Education and Resource Centre can assist you to access information, advice and resources about HIV. We provide this for people living with HIV, those affected by HIV, health and community workers and the general community.</p>
      <a class="btn btn-blue" href="#">Learn More →</a>
    </div>
  </div>
</section>

<section class="what">
  <div class="wrap">
    <div class="what-frame"></div>
    <div class="what-photo" role="img" aria-label="Microscope rendering of a virus particle in blue tones"></div>
    <div class="what-body">
      <h2 class="heading">What Is <b>HIV?</b></h2>
      <p class="lead"><span>HIV</span> is the name of a virus that attacks the body’s immune (defense) system.</p>
      <p><strong>H — Human:</strong> This particular virus is found only in humans.</p>
      <p><strong>I — Immunodeficiency:</strong> This particular virus is found only in humans.</p>
      <p><strong>V — Virus:</strong> This is a tiny, infection-causing particle that takes over other cells to grow and spread.</p>
      <p>The body’s immune system cannot fight off HIV by itself. It needs help from medicine to fight HIV. Without medicine, HIV damages and eventually causes serious damage to the immune system. At this point, HIV progresses to AIDS.</p>
      <a class="btn btn-purple" href="#">Learn More →</a>
    </div>
  </div>
</section>

<section class="topics">
  <div class="wrap">
    <h2 class="heading section-title">About HIV <b>Learning Hub</b></h2>
    <p class="section-sub">Clear and reliable information on all aspects of HIV.</p>
    <div class="cards">
      <article class="card">
        <div class="card-img" role="img" aria-label="Unwell woman resting on a sofa" style="background:linear-gradient(135deg,#c9a36a,#7d7a78 60%,#4a4a4a)"></div>
        <h3>HIV Signs and symptoms</h3>
        <p>The symptoms of HIV vary depending on the stage of infection. he disease spreads more easily in the...</p>
        <a class="more" href="#">Learn More →</a>
      </article>
      <article class="card">
        <div class="card-img" role="img" aria-label="Microscopic view of a cell being injected" style="background:radial-gradient(circle at 50% 50%,#e06a8a,#5b8fd6 50%,#1e3f8a)"></div>
        <h3>HIV Transmission</h3>
        <p>HIV can be transmitted via the exchange of a variety of body fluids from people living with HIV, such...</p>
        <a class="more" href="#">Learn More →</a>
      </article>
      <article class="card">
        <div class="card-img" role="img" aria-label="Red ribbon beside a condom on a lilac background" style="background:radial-gradient(circle at 45% 50%,#d9332d,#b7aee0 45%,#c9c2ea)"></div>
        <h3>Risk Factors</h3>
        <p>Behaviours and conditions that put people at greater risk of contracting HIV include...</p>
        <a class="more" href="#">Learn More →</a>
      </article>
      <article class="card">
        <div class="card-img" role="img" aria-label="Gloved hands handling a blood sample in a lab" style="background:linear-gradient(135deg,#eef0f2,#b9c2cc 55%,#3c5aa8)"></div>
        <h3>HIV Diagnosis</h3>
        <p>HIV can be diagnosed through rapid diagnostic tests that provide same-day results. This greatly facilitates...</p>
        <a class="more" href="#">Learn More →</a>
      </article>
      <article class="card">
        <div class="card-img" role="img" aria-label="Doctor holding a red ribbon in cupped hands" style="background:radial-gradient(circle at 50% 60%,#d8302a,#e9ecef 45%,#cfd6dc)"></div>
        <h3>HIV Prevention</h3>
        <p>HIV is a preventable disease. Reduce the risk of HIV infection by: using a male or female condom...</p>
        <a class="more" href="#">Learn More →</a>
      </article>
      <article class="card">
        <div class="card-img" role="img" aria-label="Medicine bottles and a pink ribbon beside a calendar" style="background:linear-gradient(135deg,#c9b59a,#6e7074 50%,#c86cc0)"></div>
        <h3>HIV Treatment</h3>
        <p>There is no cure for HIV infection. It is treated with antiretroviral drugs, which stop the virus from replicating...</p>
        <a class="more" href="#">Learn More →</a>
      </article>
    </div>
    <a class="btn btn-blue" href="#">Load More →</a>
  </div>
</section>

<section class="cta">
  <div class="cta-hands" role="img" aria-label="Open hands holding a red ribbon"></div>
  <div class="cta-people" role="img" aria-label="Paper cut-out family holding hands"></div>
  <div class="cta-body">
    <h2 class="heading">Let’s Stop <b>HIV Together</b></h2>
    <p>Get tailored information about your risk and<br>learn how to protect yourself.</p>
    <a class="btn" href="#">Download Resources →</a>
  </div>
</section>

<section class="stages">
  <div class="wrap">
    <h2 class="heading section-title">What Are The <b>Stages Of HIV?</b></h2>
    <p class="section-sub">When people with HIV don’t get treatment, they typically progress through three stages.</p>
    <div class="video">
      <div class="video-still" role="img" aria-label="Video still of a raised hand with a blue ribbon drawn on the palm"></div>
      <svg class="play" width="120" height="120" viewBox="0 0 120 120" aria-hidden="true">
        <defs><path id="ring" d="M60,60 m-40,0 a40,40 0 1,1 80,0"/></defs>
        <text font-family="Poppins,sans-serif" font-size="11" fill="#fff" letter-spacing="1.5"><textPath href="#ring" startOffset="12%">WATCH OUR VIDEO</textPath></text>
        <circle cx="60" cy="60" r="22" fill="#fff"/>
        <path d="M54 50 L70 60 L54 70 Z" fill="#1b2a3a"/>
      </svg>
    </div>
  </div>
</section>

<section class="blogs">
  <div class="wrap">
    <h2 class="heading section-title">Latest <b>Blogs</b></h2>
    <article class="feature">
      <div class="feature-img" role="img" aria-label="Doctor consulting with a patient at a desk"></div>
      <div class="meta"><span>HIV Diagnosis</span>23.09.2023</div>
      <h3>If I Test Positive for HIV and Have No Health Coverage, Am I Screwed?</h3>
      <p>Lorem ipsum dolor sit amet, consectetuer adipiscing elit, sed mol diam nonummy nibh euismod tincidunt ut laoreet dolore magna aliquam erat volutpat.</p>
      <a class="more" href="#">Learn More →</a>
    </article>
    <div class="posts">
      <article class="post">
        <div class="post-img" role="img" aria-label="Hand with a red ribbon on a yellow background" style="background:radial-gradient(circle at 50% 50%,#d2332c,#e8b04a 50%,#f0c35a)"></div>
        <div>
          <div class="meta"><span>HIV Advocacy &amp; Activism</span>23.09.2023</div>
          <h4>It’s Time for a #MeToo Revolution in HIV Advocacy</h4>
          <p>Duis autem vel eum iriure dolor in mork hendrerit in vulputate velit esse...</p>
          <a class="more" href="#">Learn More →</a>
        </div>
      </article>
      <article class="post">
        <div class="post-img" role="img" aria-label="Person holding pills and a glass of water" style="background:linear-gradient(135deg,#d9d9d9,#8a8f96 60%,#3b3f45)"></div>
        <div>
          <div class="meta"><span>Basics on Living Well</span>23.09.2023</div>
          <h4>People Living With HIV Deserve Better at Pharmacies</h4>
          <p>Duis autem vel eum iriure dolor in mork hendrerit in vulputate velit esse...</p>
          <a class="more" href="#">Learn More →</a>
        </div>
      </article>
      <article class="post">
        <div class="post-img" role="img" aria-label="Woman enjoying a healthy salad at home" style="background:linear-gradient(135deg,#6c7a4a,#c9a07a 50%,#efe6da)"></div>
        <div>
          <div class="meta"><span>Basics on Living Well</span>23.09.2023</div>
          <h4>Getting Good (and Avoiding Bad) Nutrition Advice for HIV Care</h4>
          <p>Duis autem vel eum iriure dolor in mork hendrerit in vulputate velit esse...</p>
          <a class="more" href="#">Learn More →</a>
        </div>
      </article>
    </div>
    <a class="btn btn-blue" href="#">Load More →</a>
  </div>
</section>

<section class="newsletter">
  <div class="wrap">
    <h2 class="heading">Check Out <b>HIV Learning Hub Newsletter</b></h2>
    <p>Get the latest info on everything related to HIV/AIDS.</p>
    <div class="signup">
      <span><svg width="14" height="11" viewBox="0 0 14 11" aria-hidden="true"><rect x=".5" y=".5" width="13" height="10" rx="1" fill="none" stroke="#999"/><path d="M1 1 L7 6 L13 1" fill="none" stroke="#999"/></svg>Email address</span>
      <a class="btn" href="#">Sign Up →</a>
    </div>
  </div>
</section>

<footer class="site-footer">
  <div class="wrap">
    <a class="brand" href="#"><span class="brand-dot"></span>HIV Learning Hub</a>
    <div class="foot-about">
      <p><strong>HIV Learning Hub</strong> changes lives by sharing information about HIV &amp; AIDS. We provide independent, accurate &amp; accessible information about HIV.</p>
      <a class="more" href="#">Learn More →</a>
    </div>
    <div class="foot-col" style="left:330px">
      <h5>Quick <b>Links</b></h5>
      <ul>
        <li><a class="active" href="#">Home</a></li>
        <li><a href="#">HIV</a></li>
        <li><a href="#">Treatment</a></li>
        <li><a href="#">Prevention</a></li>
        <li><a href="#">Resources</a></li>
        <li><a href="#">Contact</a></li>
      </ul>
    </div>
    <div class="foot-col" style="left:490px;width:220px">
      <h5>Contact <b>Details</b></h5>
      <div class="contact-row">
        <svg width="12" height="16" viewBox="0 0 12 16" aria-hidden="true"><path d="M6 0a6 6 0 0 1 6 6c0 4-6 10-6 10S0 10 0 6a6 6 0 0 1 6-6z" fill="var(--magenta)"/><circle cx="6" cy="6" r="2.2" fill="#fff"/></svg>
        <div><strong>HIV Learning Hub</strong><br>123, Loream Ipsum Dollar Smit,<br>Larotee. AB - 123 456</div>
      </div>
      <div class="contact-row" style="align-items:center">
        <svg width="14" height="14" viewBox="0 0 14 14" aria-hidden="true"><path d="M3 0l2.5 3-1.5 2a8 8 0 0 0 5 5l2-1.5 3 2.5-1.5 2.5C6 14 0 8 .5 1.5z" fill="var(--magenta)"/></svg>
        <strong style="letter-spacing:1px">123 456 7890</strong>
      </div>
      <div class="contact-row" style="align-items:center">
        <svg width="14" height="11" viewBox="0 0 14 11" aria-hidden="true"><rect width="14" height="11" rx="1" fill="var(--magenta)"/><path d="M1 1.5 L7 6 L13 1.5" fill="none" stroke="#fff"/></svg>
        <span>info@hivlearninghub.org</span>
      </div>
    </div>
    <div class="foot-col" style="left:771px">
      <h5>Follow <b>Us</b></h5>
      <div class="social"><i></i>Facelist</div>
      <div class="social"><i></i>Chatter</div>
      <div class="social"><i></i>Linkup</div>
    </div>
  </div>
  <div class="copyright">Copyright 2023 HIV Learning Hub. All Rights Reserved.</div>
</footer>

</body>
</html>
```